KVO-Business Card Design

I need a modern, professional business card design that includes my logo as the main feature, maybe the entire background with the contact info overlaying or even contact info on the back and the logo full frontal

Neat and organized placement of contact information

Would like to see options in black and white

Target Market(s)

real estate Developers, Construction managers, business and home owners

Industry/Entity Type

Construction

Contact Information for Business Card

KVO Construction
Danny Ferrante
General Contractor

Office: 1-888-902-7315 Ext #1
Cell: 215-730-4162
Fax: 1-888-902-7315

Font styles to use
Serif

Requirements
Must have
• title
• office #
• cell #
• Email
• website
Nice to have
• fax

```html
<!DOCTYPE html>
<html lang="en">
<head>
<meta charset="utf-8">
<title>KVO Construction – Business Card</title>
<link rel="stylesheet" href="https://fonts.googleapis.com/css2?family=Arimo:wght@400;700&display=swap">
<style>
  :root {
    --page-bg: #e6e6e4;
    --card-white: #ffffff;
    --card-black: #000000;
    --ink: #111111;
    --brand-green: #3fae49;
    --brand-green-faint: rgba(90, 160, 80, 0.22);
    --tagline-grey: #a3a3a3;
    --tagline-white: #f2f2f2;
    --card-shadow: 0 10px 28px rgba(0, 0, 0, 0.22);
  }
  * { box-sizing: border-box; margin: 0; padding: 0; }
  html, body {
    width: 1200px;
    height: 1200px;
    overflow: hidden;
    background: var(--page-bg);
    font-family: "Arimo", Arial, sans-serif;
  }
  .sheet {
    position: relative;
    width: 1200px;
    height: 1200px;
  }
  .card {
    position: absolute;
    left: 150px;
    width: 900px;
    height: 514px;
    box-shadow: var(--card-shadow);
    overflow: hidden;
  }
  /* Contact side */
  .card--contact {
    top: 50px;
    background: var(--card-white);
    color: var(--ink);
  }
  .contact__watermark {
    position: absolute;
    left: 190px;
    top: 170px;
    font-weight: 700;
    font-size: 250px;
    line-height: 1;
    letter-spacing: -6px;
    color: var(--brand-green-faint);
    user-select: none;
  }
  .contact__watermark-tagline {
    position: absolute;
    left: 196px;
    top: 430px;
    font-size: 19px;
    letter-spacing: 6px;
    text-transform: uppercase;
    color: var(--tagline-grey);
  }
  .contact__name {
    position: absolute;
    left: 46px;
    top: 38px;
    font-weight: 700;
    font-size: 78px;
    letter-spacing: -1px;
  }
  .contact__title {
    position: absolute;
    left: 92px;
    top: 128px;
    font-weight: 700;
    font-size: 52px;
    letter-spacing: -0.5px;
  }
  .contact__phones {
    position: absolute;
    left: 46px;
    top: 250px;
    display: grid;
    grid-template-columns: 62px auto;
    row-gap: 4px;
    font-weight: 700;
    font-size: 19px;
  }
  .contact__web {
    position: absolute;
    right: 60px;
    bottom: 46px;
    text-align: left;
    font-weight: 700;
    font-size: 21px;
    line-height: 1.25;
  }
  /* Brand side */
  .card--brand {
    top: 636px;
    background: var(--card-black);
  }
  .brand__mark {
    position: absolute;
    left: 0;
    right: 0;
    top: 100px;
    display: flex;
    align-items: center;
    justify-content: center;
    gap: 22px;
  }
  .brand__square {
    width: 40px;
    height: 40px;
    background: var(--brand-green);
  }
  .brand__name {
    font-weight: 700;
    font-size: 210px;
    line-height: 1;
    letter-spacing: -4px;
    color: var(--brand-green);
  }
  .brand__tagline {
    position: absolute;
    left: 0;
    right: 0;
    top: 360px;
    text-align: center;
    font-size: 22px;
    letter-spacing: 7px;
    text-transform: uppercase;
    color: var(--tagline-white);
  }
</style>
</head>
<body>
<main class="sheet">
  <section class="card card--contact" aria-label="Contact side of business card">
    <div class="contact__watermark" aria-hidden="true">KVO</div>
    <div class="contact__watermark-tagline" aria-hidden="true">Keystone Valley Renovations</div>
    <h1 class="contact__name">Danny Ferrante</h1>
    <p class="contact__title">General Contractor</p>
    <dl class="contact__phones">
      <dt>Office:</dt><dd>1-888-902-7315 Ext #1</dd>
      <dt>Fax:</dt><dd>1-888-902-7315</dd>
      <dt>Cell:</dt><dd>215-730-4162</dd>
    </dl>
    <p class="contact__web">e-mail address<br>Website</p>
  </section>

  <section class="card card--brand" aria-label="Brand side of business card">
    <div class="brand__mark">
      <span class="brand__square" aria-hidden="true"></span>
      <span class="brand__name">KVO</span>
    </div>
    <p class="brand__tagline">Keystone Valley Renovations</p>
  </section>
</main>
</body>
</html>
```